Article/Flyer - Reservation of Rights

We would like an article that we normally produce through illustrator in a pdf format to be placed in a Word format. We have provided a sample article/flyer of our normal distribution style. We would like the outcome to be in WORD format

```html
<!DOCTYPE html>
<html lang="en">
<head>
<meta charset="utf-8">
<title>Reservation of Rights – Aldren &amp; Company</title>
<link href="https://fonts.googleapis.com/css2?family=Lato:wght@400;700&display=swap" rel="stylesheet">
<style>
  :root {
    --frame: #1b1b1b;
    --footer-bar: #3a3b3d;
    --paper: #ffffff;
    --ink: #2b2b2b;
    --accent: #8b1e2e;
    --sky-light: #e6f2f9;
    --sky-mid: #a9cfe6;
    --sky-deep: #6b9fc4;
  }
  * { margin: 0; padding: 0; box-sizing: border-box; }
  html, body { width: 900px; height: 1200px; overflow: hidden; background: var(--frame); }
  body { font-family: "Lato", Arial, sans-serif; color: var(--ink); position: relative; }

  .page {
    position: absolute; left: 39px; top: 68px; width: 822px; height: 1042px;
    background: var(--paper); overflow: hidden;
  }
  .footer-bar {
    position: absolute; left: 39px; top: 1110px; width: 822px; height: 22px;
    background: var(--footer-bar);
  }

  .masthead { position: absolute; left: 0; top: 0; width: 822px; height: 300px; }
  .masthead-photo {
    position: absolute; inset: 0;
    background:
      linear-gradient(115deg, transparent 55%, rgba(80,130,170,.35) 75%, rgba(60,110,150,.5) 100%),
      linear-gradient(180deg, var(--sky-mid) 0%, var(--sky-light) 55%, #ffffff 100%);
  }
  .masthead-curve { position: absolute; left: 0; top: 250px; width: 822px; height: 80px; }

  .brand { position: absolute; left: 35px; top: 40px; }
  .brand-name {
    font-size: 41px; font-weight: 400; letter-spacing: 0.5px; color: #1f1f1f;
    text-transform: uppercase; line-height: 1;
  }
  .brand-tagline { font-size: 13.6px; color: #2a2a2a; margin-top: 6px; }

  .column { position: absolute; width: 342px; }
  .column-left { left: 46px; top: 313px; }
  .column-right { left: 435px; top: 312px; }
  .wide { position: absolute; left: 46px; top: 860px; width: 731px; }

  p {
    font-size: 12.3px; line-height: 16.2px; text-align: justify; margin-bottom: 8px;
  }
  .intro { margin-bottom: 48px; }
  h2 {
    font-size: 15.6px; font-weight: 400; color: var(--accent); margin-bottom: 12px; line-height: 1.2;
  }
  .column-right h2 { margin-bottom: 11px; }
</style>
</head>
<body>
  <div class="page">
    <header class="masthead">
      <div class="masthead-photo" role="img" aria-label="Photograph looking up at glass office towers against a pale blue sky"></div>
      <svg class="masthead-curve" viewBox="0 0 822 80" preserveAspectRatio="none" aria-hidden="true">
        <path d="M0 14 C 150 46, 300 52, 450 36 C 600 20, 720 20, 822 30 L822 80 L0 80 Z" fill="#ffffff"/>
        <path d="M0 14 C 150 46, 300 52, 450 36 C 600 20, 720 20, 822 30" fill="none" stroke="var(--accent)" stroke-width="7"/>
      </svg>
      <div class="brand">
        <div class="brand-name">Aldren &amp; Company</div>
        <div class="brand-tagline">Serving Architects, Engineers and Environmental Consultants</div>
      </div>
    </header>

    <section class="column column-left">
      <p class="intro">Reporting a claim or potential claim to your professional liability insurance company will trigger a fair amount of return correspondence that often creates confusion rather than clarity. One document that commonly falls into this category is the Reservation of Rights Letter.</p>

      <h2>What is the Reservation of Rights Letter</h2>
      <p>The Reservation of Rights Letter is a normal part of the insurance claims process. Its purpose is to provide notification from the insurance company to the policy holder that coverage may not apply. While this often comes as alarming news, the Reservation of Rights Letter should not be mistaken as an outright denial -- it does not automatically mean that coverage is being or will be denied.</p>
      <p>This standard correspondence is routinely sent to comply with state laws and preserve the insurance company's legal ability to deny some, or all, of the claim pending further investigation while the claim is ongoing and being handled by the insurance company. Failure to send the letter could be considered a waiver of their rights at a later time.</p>
      <p>Because information is vague in the early stages of a claim and often is limited to unsubstantiated allegations and a few facts, the Reservation of Rights Letter protects the insurance company's interests to later deny coverage in whole or part based on evidence revealed during claims handling.</p>
    </section>

    <section class="column column-right">
      <h2>Interpreting the Letter</h2>
      <p>Most of the time the Reservation of Rights Letter is a generic form letter that states your insurance company is proceeding with handling your claim but reserves the right to deny coverage later on based upon any information that reveals reason to deny.</p>
      <p>Legitimate reasons an insurance company may deny coverage include when the loss occurred in relation to your retroactive date, specific exclusions in the policy language, prior knowledge of the incident, and coverage by another policy, among others.</p>
      <p>If the insurance company believes there may be reason for denial at the time the Reservation of Rights Letter is sent, it will be stated in the letter. For example, if the claim alleges breach of warranty, the letter will state that warranties are specifically excluded by the policy and it will include the policy language to demonstrate the exclusion.</p>
      <p>Even when specific reasons for potential coverage denial are cited, it is important to note that this is not a final verdict nor does it mean complete lack of coverage. Generally the insurance company is obligated to help you if any of your claims are covered by your insurance policy – there is a duty to defend. In cases such as the scenario above, circumstances of the claim will influence what is covered and what may be subject to exclusion.</p>
      <p>Based on investigative conclusions, the insurance company may not be obligated to pay the damages for certain types or aspects of claims.</p>
    </section>

    <section class="wide">
      <h2>How to Proceed</h2>
      <p>Although the intent of the Reservation of Rights Letter is to protect the insurance company's interests, it also alerts the policy holder to the fact that some elements of a claim may not be covered and therefore allows the insured to take steps to protect its potentially uninsured interests.</p>
      <p>However, receiving the Reservation of Rights Letter and even the insurance company's interpretation of the policy language or law that they believe points toward coverage declination does not mean that you are automatically required to accept a denial of coverage.</p>
      <p>The best thing to do upon receiving the letter is to contact your broker and work closely with them and the insurance company claims handling department to ensure the prompt and fair handling of your claim.</p>
    </section>
  </div>
  <div class="footer-bar"></div>
</body>
</html>
```